Uncoded website + logo for game server company

We're looking to refresh our website - plinthware.net. We are a server provider that specializes in Tilecraft servers, as well as voice servers. Our primary goal is to keep the same essential layout but get a more modern, updated, and smooth look; our current site is a bit cluttered and unprofessional, and doesn't lend too well to ease of use.

Our color scheme is blue and white, though the shade of blue can vary. We are happy to experiment with other colors as well, but blue is recognized as our main color. The shades in use on our current site are a good starting point.

We would like the design to be flat and modern, sleek, and clean. Since we provide services relating to Tilecraft, some sort of integration with Tilecraft themes would be preferable; eg. elements from the game. The design should not be overly professional as we serve primary a young demographic, but it should still convey a sense of professionalism in that our network and infrastructure is solid.

For our logo, we would like a geometric/cube-based design. We would like to see "PlinthWare" used within the logo, rather than "7Ware" as it is now. A flat design would be preferred with single or two-tone color scheme using blue/black/white and perhaps other small accent colors. An icon/symbol integrated with the logo would suit us very well.

We would love to keep in contact with the winning designer and continue work on both our current website and other websites in the future.
Please email marcel@plinthware.net with any additional questions.

** Colors listed are examples that we like, not required **
** No HTML/CSS/JS is required to be submitted; we only need the design. ***

Feel free to submit a single page design for review and we will determine if a full design is necessary. If you choose to do this, please use the home page and/or the Tilecraft page.
Updates

Target Market(s)

Our target demographic is comprised of young (14 - 24 y/o) gamers and community owners. Because of the audience, the design should be easy to follow and not overly complicated; should be straightforward with its features and options.

Industry/Entity Type

It Company

Font styles to use
Sans Serif

Colors
3276b5
0092cd
ceddec
cde9f5
ecf7fa
ffffff
85abd2

Requirements
Must have
• Required pages:
- Home page with main features and news/updates
- Tilecraft page with features and customization options
- Tilecraft VPS page, similar to Tilecraft page
- Voice servers page with features and customization options
- Dedicated servers page with package listings and features + customization options
- Stub page for other basic pages (ToS/AUP/Careers)

Product pages (Tilecraft/voice/dedicated):
- Product overview area with area for summary
- Features area for overview of all included features (such as on current site - see Tilecraft)
- Customization options (eg. value sliders) with price display and list of features
Nice to have
• A slider on the front page would be nice, based on HTML elements rather than images as we do not have a graphic designer (utilizing text and background color/texture elements vs fully designed images).
An area for testimonials/quotes from customers
Social icons

```html
<!DOCTYPE html>
<html lang="en">
<head>
<meta charset="utf-8">
<title>PlinthWare – Game Server Hosting</title>
<link rel="stylesheet" href="https://fonts.googleapis.com/css2?family=Open+Sans:wght@400;600;700;800&display=swap">
<style>
:root{
  --blue:#0092cd;
  --blue-deep:#3276b5;
  --blue-navy:#1d5d97;
  --blue-dark:#164a7a;
  --blue-mid:#85abd2;
  --tint-1:#ceddec;
  --tint-2:#cde9f5;
  --tint-3:#ecf7fa;
  --white:#ffffff;
  --ink:#2b3a4a;
  --muted:#6d7f90;
}
*{box-sizing:border-box;margin:0;padding:0}
html,body{width:828px;height:1200px;overflow:hidden}
body{font-family:"Open Sans",Arial,sans-serif;color:var(--ink);background:var(--white);position:relative}

/* hero */
.hero{position:absolute;left:0;top:0;width:828px;height:325px;background:linear-gradient(180deg,#1aa3dc 0%,var(--blue) 100%);overflow:hidden}
.brand{position:absolute;left:40px;top:16px;display:flex;align-items:center;gap:8px;background:var(--white);padding:8px 14px;border-radius:4px}
.brand-square{width:22px;height:22px;background:var(--blue-deep)}
.brand-name{font-weight:800;font-size:20px;color:var(--blue-deep);letter-spacing:.5px}
.utility{position:absolute;right:40px;top:12px;display:flex;gap:14px;font-size:10px;color:var(--white);align-items:center}
.utility svg{width:10px;height:10px}
.top-nav{position:absolute;right:40px;top:42px;display:flex;gap:6px}
.top-nav a{font-size:11px;font-weight:600;color:var(--white);text-decoration:none;padding:5px 12px;text-transform:uppercase}
.top-nav a.active{background:var(--tint-2);color:var(--blue-deep);border-radius:2px}
.hero-copy{position:absolute;left:62px;top:100px;color:var(--white)}
.hero-copy h1{font-size:36px;font-weight:400;line-height:1.15}
.hero-copy .app{font-size:19px;font-weight:700;margin-top:12px}
.hero-copy .soon{font-size:13px;opacity:.9}
.btn-outline{display:inline-block;margin-top:22px;border:2px solid var(--white);color:var(--white);font-size:18px;padding:8px 36px;border-radius:3px}
.hero-visual{position:absolute;left:480px;top:78px;width:250px;height:247px;border-radius:14px 14px 0 0;background:linear-gradient(160deg,#e8f4fb 0%,#b9d9ee 60%,#8fbfe0 100%)}
.arrow{position:absolute;width:26px;height:26px}
.hero .arrow{top:152px}

/* main nav */
.main-nav{position:absolute;left:0;top:325px;width:828px;height:32px;background:var(--blue-deep);display:flex;justify-content:center}
.main-nav a{color:var(--white);font-size:11px;font-weight:600;text-decoration:none;padding:0 22px;line-height:32px;border-right:1px solid rgba(255,255,255,.35)}
.main-nav a:last-child{border-right:none}

/* features */
.features{position:absolute;left:0;top:357px;width:828px;height:283px;background:var(--tint-3)}
.feature-grid{position:absolute;left:48px;top:12px;width:500px;display:grid;grid-template-columns:1fr 1fr;gap:6px}
.feature{height:126px;padding:12px 14px;color:var(--white)}
.feature:nth-child(1){background:var(--blue)}
.feature:nth-child(2){background:#1c86c4}
.feature:nth-child(3){background:#2f7dbd}
.feature:nth-child(4){background:var(--blue-deep)}
.feature-head{display:flex;align-items:center;gap:8px}
.feature-head svg{width:30px;height:30px;flex:none}
.feature h3{font-size:15px;font-weight:800;text-transform:uppercase}
.feature p{font-size:9px;line-height:1.45;margin-top:6px;opacity:.92}
.sidebar{position:absolute;left:560px;top:12px;width:218px;display:flex;flex-direction:column;gap:6px}
.promo{background:var(--blue-deep);color:var(--white);text-align:center;padding:9px 12px}
.promo h4{font-size:12px;font-weight:800;text-transform:uppercase;line-height:1.25}
.promo p{font-size:11px;font-weight:600;line-height:1.3;margin-top:4px}
.promo.trial{background:var(--blue-navy)}
.subscribe{background:var(--blue);color:var(--white);padding:9px 12px}
.subscribe h4{font-size:12px;font-weight:800;text-transform:uppercase}
.subscribe p{font-size:8px;margin-top:3px}
.sub-form{display:flex;margin-top:7px}
.sub-form span{flex:1;background:var(--white);color:var(--muted);font-size:8px;padding:5px 6px}
.sub-form b{background:var(--blue-dark);font-size:8px;padding:5px 10px}

/* testimonials */
.testimonials{position:absolute;left:0;top:640px;width:828px;height:335px}
.testimonials h2{text-align:center;font-size:20px;font-weight:400;color:var(--ink);margin-top:22px;text-transform:uppercase}
.testimonials h2::after{content:"";display:block;width:60px;height:2px;background:var(--blue);margin:6px auto 0}
.quote-row{position:absolute;left:110px;top:110px;width:608px;display:flex;gap:26px;align-items:center}
.client-photo{width:96px;height:96px;border-radius:50%;flex:none;background:linear-gradient(160deg,#c9d6e2,#7f95aa)}
.quote p{font-size:11px;font-style:italic;color:var(--muted);line-height:1.55}
.quote cite{display:block;margin-top:8px;font-size:11px;font-style:normal;font-weight:700;color:var(--ink)}
.testimonials .arrow{top:145px}
.btn-solid{position:absolute;left:304px;top:268px;width:220px;height:42px;background:var(--blue);color:var(--white);font-size:17px;text-align:center;line-height:42px;text-transform:uppercase}

/* footer */
.site-footer{position:absolute;left:0;top:975px;width:828px;height:120px;background:var(--blue-deep);color:var(--white)}
.footer-cols{display:grid;grid-template-columns:repeat(4,1fr);padding:20px 48px 0}
.footer-cols h5{font-size:11px;font-weight:700;text-transform:uppercase;margin-bottom:8px}
.footer-cols p{font-size:9px;line-height:1.7;opacity:.9}
.socials{display:flex;gap:6px;margin-top:6px}
.socials span{width:22px;height:22px;background:var(--white);opacity:.9;border-radius:3px}
.legal-note{position:absolute;left:0;top:1095px;width:828px;height:105px;background:var(--blue-dark);color:var(--tint-1);font-size:9px;line-height:1.6;padding:22px 48px}
</style>
</head>
<body>

<header class="hero">
  <div class="brand"><span class="brand-square"></span><span class="brand-name">PlinthWare</span></div>
  <div class="utility">
    <span>Login</span>
    <svg viewBox="0 0 10 10"><path d="M2 1l2 2-1 1.2a6 6 0 0 0 2.8 2.8L7 6l2 2-1.2 1.5C4.5 9 1 5.5.5 2.2z" fill="#fff"/></svg>
    <span>555.014.2290</span>
  </div>
  <nav class="top-nav">
    <a class="active" href="#">Panel</a><a href="#">Blog</a><a href="#">News</a><a href="#">Support</a>
  </nav>
  <svg class="arrow" style="left:14px" viewBox="0 0 26 26"><path d="M16 5l-8 8 8 8" stroke="#fff" stroke-width="2.5" fill="none"/></svg>
  <div class="hero-copy">
    <h1>Manage your servers<br>anytime, anywhere</h1>
    <div class="app">Official PlinthWare Mobile app</div>
    <div class="soon">coming soon to phones and tablets</div>
    <span class="btn-outline">Learn More</span>
  </div>
  <div class="hero-visual" role="img" aria-label="Hand holding a tablet showing the PlinthWare app"></div>
  <svg class="arrow" style="right:14px" viewBox="0 0 26 26"><path d="M10 5l8 8-8 8" stroke="#fff" stroke-width="2.5" fill="none"/></svg>
</header>

<nav class="main-nav">
  <a href="#">HOME</a><a href="#">TILECRAFT</a><a href="#">VOICE</a><a href="#">WEB</a><a href="#">DEDICATED</a><a href="#">FAQ</a><a href="#">CONTACT</a>
</nav>

<section class="features">
  <div class="feature-grid">
    <article class="feature">
      <div class="feature-head">
        <svg viewBox="0 0 30 30"><circle cx="15" cy="15" r="9" fill="none" stroke="#fff" stroke-width="3" stroke-dasharray="4 3"/><circle cx="15" cy="15" r="4" fill="#fff"/></svg>
        <h3>Instant Setup</h3>
      </div>
      <p>Your game server goes live within seconds of checkout. Pick a version, choose your plugins, and start building with friends right away, no waiting or tickets.</p>
    </article>
    <article class="feature">
      <div class="feature-head">
        <svg viewBox="0 0 30 30"><path d="M8 22h15a5 5 0 0 0 0-10 7 7 0 0 0-13-1 5.5 5.5 0 0 0-2 11z" fill="#fff"/></svg>
        <h3>Automatic Backups</h3>
      </div>
      <p>We save your world every few hours to separate storage, so a crash or griefing never costs you days of work. Restore any snapshot with one click.</p>
    </article>
    <article class="feature">
      <div class="feature-head">
        <svg viewBox="0 0 30 30"><circle cx="11" cy="10" r="4" fill="#fff"/><circle cx="20" cy="10" r="4" fill="#fff"/><path d="M3 24a8 8 0 0 1 16 0zM13 24a8 8 0 0 1 15 0z" fill="#fff"/></svg>
        <h3>Awesome Support</h3>
      </div>
      <p>Our team is here to help, day or night. Reach us through live chat, tickets or the forums and get a friendly reply from real players.</p>
    </article>
    <article class="feature">
      <div class="feature-head">
        <svg viewBox="0 0 30 30"><rect x="8" y="8" width="14" height="14" fill="none" stroke="#fff" stroke-width="2.5"/><rect x="12" y="12" width="6" height="6" fill="#fff"/><path d="M12 3v4M18 3v4M12 23v4M18 23v4M3 12h4M3 18h4M23 12h4M23 18h4" stroke="#fff" stroke-width="2"/></svg>
        <h3>Powerful Hardware</h3>
      </div>
      <p>Every node runs on fast processors, solid state drives and plenty of memory, giving your players smooth gameplay with low lag even at peak hours.</p>
    </article>
  </div>

  <aside class="sidebar">
    <div class="promo">
      <h4>Got Handheld Edition?<br>Help us test our new servers</h4>
      <p>click here to get a free handheld server today!</p>
    </div>
    <div class="promo trial">
      <h4>Want to try before you buy?</h4>
      <p>Click here for a free trial</p>
    </div>
    <div class="subscribe">
      <h4>Subscribe Newsletter</h4>
      <p>Get monthly updates, new offers and server tips sent to your inbox.</p>
      <div class="sub-form"><span>Type your email here</span><b>Go</b></div>
    </div>
  </aside>
</section>

<section class="testimonials">
  <h2>What client says about us</h2>
  <svg class="arrow" style="left:40px" viewBox="0 0 26 26"><circle cx="13" cy="13" r="12" fill="var(--tint-2)"/><path d="M15 8l-5 5 5 5" stroke="var(--blue-deep)" stroke-width="2.2" fill="none"/></svg>
  <div class="quote-row">
    <div class="client-photo" role="img" aria-label="Portrait photo of the client"></div>
    <blockquote class="quote">
      <p>“PlinthWare gave our community a fast and stable home. Setup took minutes, the panel is easy to use, and support answers quicker than any host we tried before.”</p>
      <cite>Dana Whitfield, CEO Northgate Studio</cite>
    </blockquote>
  </div>
  <svg class="arrow" style="right:40px" viewBox="0 0 26 26"><circle cx="13" cy="13" r="12" fill="var(--tint-2)"/><path d="M11 8l5 5-5 5" stroke="var(--blue-deep)" stroke-width="2.2" fill="none"/></svg>
  <span class="btn-solid">More Testimonials</span>
</section>

<footer class="site-footer">
  <div class="footer-cols">
    <div><h5>Contact Us</h5><p>555.014.2290<br>1 877 555 0190<br>marcel@plinthware.net</p></div>
    <div><h5>Quick Links</h5><p>Terms &amp; Policy<br>Terms of Service<br>Report Abuse</p></div>
    <div><h5>Social Links</h5><p>Join the Conversation</p><div class="socials"><span></span><span></span><span></span><span></span></div></div>
    <div><h5>Legal Stuff</h5><p>Copyright © 2014,<br>PlinthWare LLC,<br>All rights Reserved</p></div>
  </div>
</footer>
<div class="legal-note">PlinthWare is a Tilecraft server hosting company and is not affiliated with Blockwright AB. Tilecraft and all related names, marks and assets are property of their respective owners. All prices shown are in US dollars.</div>

</body>
</html>
```